Venture capital website it shall be called Loram Ventures

Venture capital Name is : Loram Ventures

i have already regesieted a website and comunicate the details with you when i choose a design.

i need a simple website design for a newly established venture capital. i would like something similar to the websites listed down:

http://www.tovelpark.com/

http://www.brisoltidefunds.com/

https://kpdrift.com/

http://www.mullenfield.com/

i like mullen field the most

Target Market(s)

entrepreneur - startups

Industry/Entity Type

Venture Capital

Number of Pages Required

4 page

Font styles to use
Serif
Sans Serif

Colors
ffc214
fece3e

Requirements
Must have
• the following sections:
• Philosophy (about loram Ventures)
• Team
• Knowledge
• address - contact
Nice to have
• http://www.tovelpark.com/
• http://www.brisoltidefunds.com/
• https://kpdrift.com/
• http://www.mullenfield.com/

```html
<!DOCTYPE html>
<html lang="en">
<head>
<meta charset="utf-8">
<title>Loram Ventures – Home</title>
<link href="https://fonts.googleapis.com/css2?family=Montserrat:wght@400;600;700&display=swap" rel="stylesheet">
<style>
  :root {
    --page-bg: #ffffff;
    --gold: #b8a033;
    --white: #ffffff;
    --photo-dark: #2c2c2e;
    --photo-mid: #45464a;
    --photo-warm: #3a3630;
  }
  * { box-sizing: border-box; margin: 0; padding: 0; }
  html, body {
    width: 1200px;
    height: 1200px;
    overflow: hidden;
    background: var(--page-bg);
    font-family: "Montserrat", Arial, sans-serif;
  }
  .screen {
    position: absolute;
    left: 222px;
    width: 756px;
    height: 378px;
    overflow: hidden;
  }
  .screen--closed { top: 201px; }
  .screen--open { top: 620px; }
  .hero-photo {
    position: absolute;
    inset: 0;
    background:
      radial-gradient(ellipse at 30% 45%, rgba(90,100,120,0.35), transparent 55%),
      radial-gradient(ellipse at 62% 60%, rgba(95,80,55,0.35), transparent 55%),
      linear-gradient(100deg, var(--photo-mid) 0%, var(--photo-warm) 55%, var(--photo-dark) 100%);
  }
  .shapes {
    position: absolute;
    inset: 0;
    width: 756px;
    height: 378px;
  }
  .wordmark {
    position: absolute;
    left: 231px;
    top: 150px;
    width: 296px;
    color: var(--white);
    font-weight: 700;
    text-transform: uppercase;
    white-space: nowrap;
  }
  .wordmark-name {
    display: block;
    font-size: 60px;
    line-height: 72px;
    letter-spacing: 8px;
    margin-right: -8px;
  }
  .wordmark-sub {
    display: block;
    text-align: right;
    font-size: 11px;
    line-height: 16px;
    letter-spacing: 15px;
    margin-right: -15px;
    margin-top: 2px;
  }
  .menu-label {
    position: absolute;
    left: 711px;
    top: 26px;
    color: var(--white);
    font-size: 12px;
    font-weight: 400;
  }
  .main-nav {
    position: absolute;
    left: 664px;
    top: 72px;
    list-style: none;
  }
  .main-nav li {
    color: var(--white);
    font-size: 9px;
    font-weight: 600;
    line-height: 19px;
    position: relative;
  }
  .main-nav li.is-current {
    font-size: 12px;
    font-weight: 700;
    line-height: 20px;
  }
  .main-nav li.is-current::before {
    content: "";
    position: absolute;
    left: -13px;
    top: 6px;
    border-top: 4.5px solid transparent;
    border-bottom: 4.5px solid transparent;
    border-right: 5px solid var(--white);
  }
</style>
</head>
<body>

  <section class="screen screen--closed">
    <div class="hero-photo" role="img" aria-label="Photo of a team of colleagues discussing work around a laptop, darkened"></div>
    <svg class="shapes" viewBox="0 0 756 378" aria-hidden="true">
      <polygon points="658,0 756,0 756,107" fill="var(--gold)"/>
      <circle cx="688" cy="34" r="15" fill="var(--white)"/>
      <g stroke="var(--gold)" stroke-width="1.2">
        <line x1="681" y1="30" x2="695" y2="30"/>
        <line x1="681" y1="34" x2="695" y2="34"/>
        <line x1="681" y1="38" x2="695" y2="38"/>
      </g>
    </svg>
    <span class="menu-label">Menu</span>
    <div class="wordmark">
      <span class="wordmark-name">Loram</span>
      <span class="wordmark-sub">Ventures</span>
    </div>
  </section>

  <section class="screen screen--open">
    <div class="hero-photo" role="img" aria-label="Photo of a team of colleagues discussing work around a laptop, darkened"></div>
    <svg class="shapes" viewBox="0 0 756 378" aria-hidden="true">
      <polygon points="410,0 756,0 756,378" fill="var(--gold)"/>
      <circle cx="440" cy="34" r="15" fill="var(--white)"/>
      <g stroke="var(--gold)" stroke-width="1.3">
        <line x1="435" y1="29" x2="445" y2="39"/>
        <line x1="445" y1="29" x2="435" y2="39"/>
      </g>
    </svg>
    <div class="wordmark">
      <span class="wordmark-name">Loram</span>
      <span class="wordmark-sub">Ventures</span>
    </div>
    <ul class="main-nav">
      <li class="is-current">Home</li>
      <li>About</li>
      <li>Mission</li>
      <li>Vision</li>
      <li>Values</li>
      <li>Taget Market</li>
      <li>Contact Us</li>
    </ul>
  </section>

</body>
</html>
```